Corbel Path Advisory WordPress Design

Corbel Path Advisory is a consulting company that targets small business. We use our genius in the field to help small Business navigate information systems, in particular Tallybridge Solutions.

We are looking for a WordPress Design that is playful but intelligent for our web site. The design should plays off of our Corbel Logo and be informative. The attachments is of our logo variations that will be used in your design. It should be useful to describe the look and feel of the site we are looking to get.

The color of the website is not defined yet but should work well with our logo colors.

Regarding to the template and the way to display the home page. The menu should contain the following items which will each be its own page:
1. Home Page
2. Blog
-This needs to be a frame work to allow us to constantly add written articles and Video logs with Transcripts possibly in two sections.
3. What Corbel Does
-This will contain the company approach
4. Request a Corbel
-This will be a form to collect contact information
5. Contact Corbel
6. About Us

Please keep the SIMILAR airy/mythical design used in the logo.

Finally, we need a design that will have a normal view and a mobile view.

Target Market(s)

Corbel Path Advisory is a consulting company that targets small business.

Industry/Entity Type

Business Consultant

Requirements
Must have
• Regarding to the template and the way to display the home page. The menu should contain the following items which will each be its own page:
• 1. Home Page
• 2. Blog
• -This needs to be a frame work to allow us to constantly add written articles and Video logs with Transcripts possibly in two sections.
• 3. What Corbel Does
• -This will contain the company approach
• 4. Request a Corbel
• -This will be a form to collect contact information
• 5. Contact Corbel
• 6. About Us
• Mobile View
Nice to have
• Have a magical or mythical quality like the hands around the logo but not to playful.
Should not have
• Our slogan is "Corbel solutions that make business work!"

```html
<!DOCTYPE html>
<html lang="en">
<head>
<meta charset="utf-8">
<title>Corbel Path Advisory</title>
<link rel="stylesheet" href="https://fonts.googleapis.com/css2?family=Questrial&family=Open+Sans:wght@400;600;700&display=swap">
<style>
:root{
  --ink:#1e1e1e;
  --ink-2:#2b2b2b;
  --blue:#1b93d1;
  --blue-dark:#13709f;
  --orange:#f7941d;
  --grey-band:#ececec;
  --text:#555;
  --muted:#888;
  --white:#fff;
}
*{box-sizing:border-box;margin:0;padding:0}
html,body{width:1200px;height:2216px;overflow:hidden;background:var(--white);font-family:"Open Sans",Arial,sans-serif;color:var(--text)}
.page{position:relative;width:1200px;height:2216px}
h1,h2,h3,.display{font-family:"Questrial","Century Gothic",sans-serif;font-weight:400}

/* header */
.site-header{position:absolute;left:0;top:0;width:1200px;height:184px;background:linear-gradient(#2a2a2a,#141414)}
.brand{position:absolute;left:56px;top:36px;display:flex;align-items:center;gap:18px}
.brand-mark{width:64px;height:64px;border-radius:50%;background:var(--white)}
.brand-name{font-family:"Questrial",sans-serif;font-size:36px;color:var(--white);line-height:1}
.contact-now{position:absolute;right:52px;top:44px;text-align:left}
.contact-now .label{font-family:"Questrial",sans-serif;font-size:22px;color:#ddd;letter-spacing:1px}
.contact-now .phone{font-family:"Questrial",sans-serif;font-size:32px;color:var(--orange);margin-top:2px}
.main-nav{position:absolute;left:144px;top:148px;display:flex;gap:10px}
.main-nav a{display:block;height:36px;line-height:36px;padding:0 26px;font-size:15px;color:var(--white);text-decoration:none;background:var(--orange);font-family:"Questrial",sans-serif}
.main-nav a.active{background:var(--white);color:var(--ink)}

/* hero */
.hero{position:absolute;left:0;top:184px;width:1200px;height:364px;background:radial-gradient(ellipse at 60% 45%,#3fb4e6 0%,#13709f 35%,#0a3b57 70%,#062435 100%)}
.hero-caption{position:absolute;left:0;bottom:0;width:100%;height:52px;background:rgba(0,0,0,.45);display:flex;align-items:center;justify-content:space-between;padding:0 150px}
.hero-caption h2{font-size:30px;color:#e8e8e8;letter-spacing:1px}
.dots{display:flex;gap:8px}
.dots span{width:10px;height:10px;border-radius:50%;background:#999}
.dots span.on{background:var(--white)}

/* welcome */
.welcome{position:absolute;left:150px;top:590px;width:900px;text-align:center}
.welcome h1{font-size:46px;color:var(--ink-2)}
.welcome .kicker{font-size:12px;font-weight:700;color:#444;margin-top:14px;letter-spacing:.3px}
.welcome p{font-size:12px;line-height:19px;margin-top:10px;color:var(--muted)}

.services{position:absolute;left:180px;top:900px;width:840px;display:grid;grid-template-columns:repeat(3,210px);column-gap:105px;row-gap:30px}
.service{height:190px;background:var(--blue);color:var(--white);display:flex;flex-direction:column;align-items:center;justify-content:center;text-align:center;gap:16px}
.service.featured{background:var(--orange)}
.service svg{width:40px;height:40px}
.service span{font-family:"Questrial",sans-serif;font-size:21px;line-height:25px}

/* strategies */
.strategies{position:absolute;left:0;top:1350px;width:1200px;height:350px;background:var(--grey-band)}
.strategy-list{position:absolute;left:150px;top:40px;width:230px}
.strategy-list h2{font-size:32px;color:var(--ink-2);margin-bottom:16px}
.strategy-list li{list-style:none;font-size:11px;font-weight:600;text-transform:uppercase;color:#666;line-height:24px;padding-left:14px;position:relative}
.strategy-list li::before{content:"";position:absolute;left:0;top:10px;width:5px;height:5px;background:#999}
.strategy-list li.current{color:var(--orange)}
.strategy-list li.current::before{background:var(--orange)}
.portrait{position:absolute;left:400px;top:48px;width:180px;height:200px;border:5px solid var(--white);background:linear-gradient(160deg,#e9e4df,#b9a89a 55%,#6d5a4d)}
.approach{position:absolute;left:610px;top:40px;width:440px}
.approach h2{font-size:31px;line-height:36px;color:var(--ink-2)}
.approach p{font-size:11px;line-height:17px;color:var(--muted);margin-top:8px}

/* news */
.news{position:absolute;left:150px;top:1728px;width:900px}
.news h2{font-size:32px;color:var(--ink-2);padding-bottom:12px;border-bottom:1px solid #ddd}
.news-items{display:flex;gap:40px;margin-top:22px}
.news-item{width:273px;display:flex;gap:12px}
.news-date{text-align:center;width:56px;flex:none}
.news-date .day{font-family:"Questrial",sans-serif;font-size:50px;line-height:48px;color:var(--orange)}
.news-item:nth-child(2) .day{color:var(--blue)}
.news-date .month{font-size:11px;font-weight:700;color:#444;letter-spacing:1px}
.news-item h3{font-size:22px;color:var(--ink-2)}
.news-item p{font-size:11px;line-height:16px;color:var(--muted);margin-top:4px}

/* newsletter */
.newsletter{position:absolute;left:0;top:1920px;width:1200px;height:90px;background:var(--blue);display:flex;align-items:center;padding:0 150px}
.newsletter svg{width:36px;height:26px;margin-right:16px}
.newsletter h2{font-size:26px;color:var(--white);flex:1}
.newsletter .field{width:270px;height:36px;background:var(--white);font-size:12px;color:#aaa;line-height:36px;padding-left:12px}
.newsletter .submit{width:130px;height:36px;background:var(--orange);color:var(--white);font-size:14px;font-weight:700;line-height:36px;text-align:center;margin-left:10px}

/* footer */
.site-footer{position:absolute;left:0;top:2150px;width:1200px;height:66px;background:var(--ink);display:flex;align-items:center;justify-content:space-between;padding:0 150px}
.site-footer p{font-size:12px;color:#aaa}
.site-footer strong{color:var(--white);font-weight:600}
.social{display:flex;gap:8px}
.social span{width:20px;height:20px;border-radius:50%;background:var(--orange)}
</style>
</head>
<body>
<div class="page">

  <header class="site-header">
    <div class="brand">
      <div class="brand-mark"></div>
      <div class="brand-name">Corbel Path Advisory</div>
    </div>
    <div class="contact-now">
      <div class="label">CONTACT NOW:</div>
      <div class="phone">123-555-0148</div>
    </div>
    <nav class="main-nav">
      <a class="active" href="#">Home</a>
      <a href="#">Blog</a>
      <a href="#">What Corbel Does</a>
      <a href="#">Request A Corbel</a>
      <a href="#">Contact Corbel</a>
      <a href="#">About Us</a>
    </nav>
  </header>

  <section class="hero" role="img" aria-label="Photo of glowing light bulbs hanging against a blue background">
    <div class="hero-caption">
      <h2>PROFESSIONAL CONSULTING SERVICES</h2>
      <div class="dots"><span class="on"></span><span></span><span></span><span></span></div>
    </div>
  </section>

  <section class="welcome">
    <h1>Welcome</h1>
    <div class="kicker">UNDE OMNIS ISTE NATUS ERROR SIT VOLUPTATEM ACCUSANTIUM DOLOREMQUE LAUDANTIU</div>
    <p>Sed ut perspiciatis unde omnis iste natus error sit voluptatem accusantium doloremque laudantium, totam rem aperiam, eaque ipsa quae ab illo inventore veritatis et quasi architecto beatae vitae dicta sunt explicabo. Nemo enim ipsam voluptatem quia voluptas sit aspernatur aut odit aut fugit, sed quia consequuntur magni dolores eos qui ratione voluptatem sequi nesciunt.</p>
  </section>

  <section class="services">
    <div class="service">
      <svg viewBox="0 0 40 40" fill="#fff"><path d="M4 20l8-7 6 3 6-4 12 8-3 3-5-3-8 8c-2 2-4 1-5 0L4 20z"/><rect x="2" y="14" width="5" height="10"/><rect x="33" y="14" width="5" height="10"/></svg>
      <span>Business<br>Consulting</span>
    </div>
    <div class="service featured">
      <svg viewBox="0 0 40 40" fill="none" stroke="#fff" stroke-width="3"><rect x="4" y="6" width="6" height="6"/><rect x="4" y="17" width="6" height="6"/><rect x="4" y="28" width="6" height="6"/><path d="M15 9h21M15 20h21M15 31h21"/></svg>
      <span>Enterprise<br>Application</span>
    </div>
    <div class="service">
      <svg viewBox="0 0 40 40" fill="#fff"><path d="M20 4a16 16 0 1 0 16 16H20z"/><path d="M23 2v15h15A15 15 0 0 0 23 2z"/></svg>
      <span>Sales &amp;<br>Marketing</span>
    </div>
    <div class="service">
      <svg viewBox="0 0 40 40" fill="#fff"><rect x="4" y="22" width="7" height="14"/><rect x="14" y="12" width="7" height="24"/><rect x="24" y="4" width="7" height="32"/><rect x="34" y="16" width="4" height="20"/></svg>
      <span>Finance<br>Management</span>
    </div>
    <div class="service">
      <svg viewBox="0 0 40 40" fill="#fff"><circle cx="20" cy="9" r="6"/><path d="M9 36c0-10 5-17 11-17s11 7 11 17z"/></svg>
      <span>Skills<br>&amp; Employment</span>
    </div>
    <div class="service">
      <svg viewBox="0 0 40 40" fill="none" stroke="#fff" stroke-width="2.5"><circle cx="20" cy="20" r="16"/><ellipse cx="20" cy="20" rx="7" ry="16"/><path d="M4 20h32M7 12h26M7 28h26"/></svg>
      <span>Outsourcing<br>Programs</span>
    </div>
  </section>

  <section class="strategies">
    <div class="strategy-list">
      <h2>Our Strategies</h2>
      <ul>
        <li>Sed ut perspiciatis unde</li>
        <li class="current">Omnis iste natus error</li>
        <li>Totam rem aperiam</li>
        <li>Eaque ipsa quae</li>
        <li>Quasi architecto beatae</li>
        <li>Nemo enim ipsam</li>
        <li>Sed quia consequuntur</li>
        <li>Neque porro quisquam</li>
        <li>Dolorem ipsum quia</li>
      </ul>
    </div>
    <div class="portrait" role="img" aria-label="Portrait photo of a smiling business consultant"></div>
    <div class="approach">
      <h2>Individual Approach And<br>Care About Every Client</h2>
      <p>Sed ut perspiciatis unde omnis iste natus error sit voluptatem accusantium doloremque laudantium, totam rem aperiam, eaque ipsa quae ab illo inventore veritatis et quasi architecto beatae vitae dicta sunt explicabo. Nemo enim ipsam voluptatem quia voluptas sit aspernatur aut odit aut fugit, sed quia consequuntur magni dolores eos qui ratione voluptatem sequi nesciunt.</p>
      <p>At vero eos et accusamus et iusto odio dignissimos ducimus qui blanditiis praesentium voluptatum deleniti atque corrupti quos dolores et quas molestias excepturi sint occaecati.</p>
      <p>Sed ut perspiciatis unde omnis iste natus error sit voluptatem accusantium doloremque laudantium, totam rem aperiam, eaque ipsa quae ab illo inventore veritatis et quasi architecto beatae vitae dicta sunt explicabo. Nemo enim ipsam voluptatem quia voluptas sit aspernatur aut odit aut fugit, sed quia consequuntur magni dolores eos qui ratione voluptatem sequi nesciunt.</p>
    </div>
  </section>

  <section class="news">
    <h2>What's New?</h2>
    <div class="news-items">
      <article class="news-item">
        <div class="news-date"><div class="day">15</div><div class="month">JULY</div></div>
        <div><h3>Sed Ut Perspiciatis</h3><p>Sed ut perspiciatis unde omnis iste natus error sit voluptatem accusantium doloremque.</p></div>
      </article>
      <article class="news-item">
        <div class="news-date"><div class="day">21</div><div class="month">JUNE</div></div>
        <div><h3>Sed Ut Perspiciatis</h3><p>Sed ut perspiciatis unde omnis iste natus error sit voluptatem accusantium doloremque.</p></div>
      </article>
      <article class="news-item">
        <div class="news-date"><div class="day">10</div><div class="month">JUNE</div></div>
        <div><h3>Sed Ut Perspiciatis</h3><p>Sed ut perspiciatis unde omnis iste natus error sit voluptatem accusantium doloremque.</p></div>
      </article>
    </div>
  </section>

  <section class="newsletter">
    <svg viewBox="0 0 36 26" fill="none" stroke="#fff" stroke-width="2.5"><rect x="2" y="2" width="32" height="22"/><path d="M2 2l16 13L34 2"/></svg>
    <h2>Subscribe To Our Newsletter</h2>
    <div class="field">Your Email</div>
    <div class="submit">SUBMIT</div>
  </section>

  <footer class="site-footer">
    <p>© 2013 | <strong>Corbel Path Advisory</strong> | All rights reserved.</p>
    <div class="social"><span></span><span></span><span></span><span></span></div>
  </footer>

</div>
</body>
</html>
```